Web Design Project

need a website, logo and a matching business Card for design studio. i have a company that works with many companies and i want to offer design services that will be outsourced to craftflock.

this website is totally for the design services. i need it to be simple but very catcgy and trendy, yet MUST BE ELEGENT.

you being a designer will know best what do i require in this website and how it should look and feel..

i dont need many pages, most of the selling work to clients will be face to face, this is just for them to view the sample works.

the company is called "Corvelin, Vividra Studio", so pages i need are: 1- the Studio 2- Folios 3- Contact us( will include company informaiton, and online contact form that should have a drop-down list of all types of designs.

main focus is the folios pages, it needs to have samples of works, the classification of works should be on two basis, by type of design and by designer. client should be able to select a certain designer and send an inquiry. if the customer does that, then i should get all client details and the designer should get a notification that he has been requested though no contact details of client should be given to designer as i want to make sure that those jobs are given to designer through craft flock and this is an invitation for any designer who care to put his works on the website. next to that, if the customer requires a job online then we need to get information on how design should feel and look.

please quote your price to include the website and business card design, A3 head letter and envelope.

Please provide a mock up of your design or a briefing an initial design before asking to be announced as the winner.

my customers are general managers and decision makers.

Business

• ability to filiter works based on type or designer. and website must offer all types of designs included here

```html
<!DOCTYPE html>
<html lang="en">
<head>
<meta charset="utf-8">
<title>Corvelin Vividra Studio – Browse Designs</title>
<link rel="stylesheet" href="https://fonts.googleapis.com/css2?family=Righteous&family=Quicksand:wght@400;500&family=Open+Sans:wght@400;600;700&display=swap">
<style>
:root{
  --wood:#d9a86a;
  --wood-dark:#c9925a;
  --slate:#434d56;
  --panel:#f1f1f2;
  --content:#ececed;
  --white:#ffffff;
  --ink:#2e3e4e;
  --nav:#5a6a76;
  --text:#3a3a3a;
  --link:#4a7f9c;
  --rule:#d6d8da;
  --btn-top:#dfe8ee;
  --btn-bottom:#9cb6c4;
  --btn-text:#2f4454;
}
*{box-sizing:border-box;margin:0;padding:0}
html,body{width:1200px;height:900px;overflow:hidden}
body{
  position:relative;
  font-family:"Open Sans",Arial,sans-serif;
  background:linear-gradient(90deg,var(--wood-dark),var(--wood) 30%,#dcae72 60%,var(--wood-dark));
}
.top-bar{position:absolute;left:0;top:0;width:1200px;height:36px;background:var(--slate)}
.site-footer{
  position:absolute;left:0;top:872px;width:1200px;height:28px;background:var(--slate);
  color:#e8e8e8;font-size:11px;line-height:28px;text-align:right;padding-right:52px;
}
.page{
  position:absolute;left:46px;top:36px;width:1105px;height:814px;background:var(--white);
  box-shadow:0 2px 8px rgba(0,0,0,.25);
}
.site-header{position:absolute;left:0;top:0;width:1105px;height:69px;background:var(--panel);border-bottom:1px solid var(--rule)}
.brand{position:absolute;left:32px;top:19px;display:flex;align-items:center}
.brand-name{font-family:"Righteous",sans-serif;font-size:33px;color:var(--ink);letter-spacing:4px;line-height:1}
.brand-divider{width:2px;height:26px;background:#5a8fb0;margin:0 12px 0 10px}
.brand-tag{font-family:"Quicksand",sans-serif;font-size:26px;color:var(--ink);font-weight:400;line-height:1}
.main-nav{position:absolute;right:34px;top:27px;display:flex;font-size:13.5px;font-weight:600;color:var(--nav)}
.main-nav span{padding:0 11px;border-left:1px solid #b9bfc4;line-height:14px}
.main-nav span:first-child{border-left:none}
.filter-bar{position:absolute;left:0;top:69px;width:1105px;height:47px;border-bottom:1px solid var(--rule);display:flex}
.filter{
  height:46px;border-right:1px solid var(--rule);font-size:14.5px;font-weight:600;color:#333;
  display:flex;align-items:center;position:relative;justify-content:center
}
.filter-category{width:202px}
.filter-type{width:218px}
.filter svg{position:absolute;right:16px;top:17px}
.search{
  position:absolute;right:0;top:0;width:243px;height:46px;border-left:1px solid var(--rule);
  display:flex;align-items:center;justify-content:center
}
.search-field{
  width:204px;height:30px;border:1px solid #c9cdd0;border-radius:15px;background:#fff;
  display:flex;align-items:center;padding-left:10px;font-size:12.5px;color:#8a9096;gap:6px
}
.gallery{
  position:absolute;left:0;top:116px;width:1105px;height:668px;background:var(--content);
}
.card{
  position:absolute;width:238px;height:306px;background:var(--white);
  border:1px solid #d4d6d8;box-shadow:0 1px 2px rgba(0,0,0,.08)
}
.card-art{height:185px;width:100%}
.card-body{height:86px;padding:14px 0 0 11px;color:var(--text)}
.card-title{font-size:12.5px;font-weight:700;color:#2b2b2b}
.card-type{font-size:12.5px;margin-top:6px}
.card-by{font-size:12.5px;margin-top:9px;color:#6a7680}
.card-by b{color:var(--link);font-weight:700}
.hire{
  position:absolute;left:-1px;bottom:-1px;width:238px;height:34px;
  background:linear-gradient(var(--btn-top),var(--btn-bottom));
  color:var(--btn-text);font-size:14px;font-weight:600;text-align:center;line-height:34px;
  border-top:1px solid #c3d0d8
}
.pager{
  position:absolute;left:0;top:784px;width:1105px;height:30px;background:var(--white);
  border-top:1px solid var(--rule);font-size:12.5px;font-weight:600;color:#5c6670
}
.pager-prev{position:absolute;left:12px;top:6px;display:flex;align-items:center;gap:8px}
.pager-next{position:absolute;right:12px;top:6px;display:flex;align-items:center;gap:8px}
</style>
</head>
<body>
<div class="top-bar"></div>

<div class="page">
  <header class="site-header">
    <div class="brand">
      <span class="brand-name">CORVELIN</span>
      <span class="brand-divider"></span>
      <span class="brand-tag">vividra studio</span>
    </div>
    <nav class="main-nav">
      <span>Home</span><span>Designer Portfolios</span><span>Browse Designs</span><span>Contact Us</span>
    </nav>
  </header>

  <div class="filter-bar">
    <div class="filter filter-category">Category
      <svg width="7" height="12" viewBox="0 0 7 12"><path d="M3.5 0L7 4H0z M3.5 12L0 8h7z" fill="#333"/></svg>
    </div>
    <div class="filter filter-type">All Designs
      <svg width="7" height="12" viewBox="0 0 7 12"><path d="M3.5 0L7 4H0z M3.5 12L0 8h7z" fill="#333"/></svg>
    </div>
    <div class="search">
      <div class="search-field">
        <svg width="14" height="14" viewBox="0 0 14 14"><circle cx="5.5" cy="5.5" r="4.3" fill="none" stroke="#8a9096" stroke-width="1.6"/><path d="M8.7 8.7L13 13" stroke="#8a9096" stroke-width="1.8" stroke-linecap="round"/></svg>
        Search...
      </div>
    </div>
  </div>

  <main class="gallery">
    <article class="card" style="left:37px;top:21px">
      <div class="card-art" role="img" aria-label="Business card sample in orange and grey" style="background:linear-gradient(135deg,#5b5b5b,#3a3a3a 45%,#e4572e 46%,#f06a2a 60%,#6c6c6c 61%,#2e2e2e)"></div>
      <div class="card-body"><div class="card-title">Brightcall PR - Business Cards</div><div class="card-type">Logo + Print</div><div class="card-by">by <b>Mira Lendholt</b></div></div>
      <div class="hire">Hire this Designer</div>
    </article>
    <article class="card" style="left:300px;top:21px">
      <div class="card-art" role="img" aria-label="Retro teal ribbon clothing graphic" style="background:linear-gradient(120deg,#7fd1c0,#2f9f90 40%,#1f7f77 60%,#8fd8c8)"></div>
      <div class="card-body"><div class="card-title">Retro Design Clothing</div><div class="card-type">Web</div><div class="card-by">by <b>Tobin</b></div></div>
      <div class="hire">Hire this Designer</div>
    </article>
    <article class="card" style="left:562px;top:21px">
      <div class="card-art" role="img" aria-label="Portfolio website template with pink light streaks" style="background:linear-gradient(#2c2c2c 0 18%,#f27fa3 30%,#fbd1dd 48%,#e9e3e6 60%,#3a3a3a 62%,#2a2a2a)"></div>
      <div class="card-body"><div class="card-title">Portfolio Template</div><div class="card-type">Web</div><div class="card-by">by <b>RJ Vale</b></div></div>
      <div class="hire">Hire this Designer</div>
    </article>
    <article class="card" style="left:825px;top:21px">
      <div class="card-art" role="img" aria-label="Magazine layout with red dripping paint feature" style="background:linear-gradient(90deg,#f1f1f1,#e8e8e8 30%,#d4202b 45%,#b5121c 70%,#eeeeee 72%)"></div>
      <div class="card-body"><div class="card-title">Pivot Magazine Layout</div><div class="card-type">Print</div><div class="card-by">by <b>Hugo Brin</b></div></div>
      <div class="hire">Hire this Designer</div>
    </article>

    <article class="card" style="left:37px;top:348px">
      <div class="card-art" role="img" aria-label="Editorial magazine spread with orange and pink stripes" style="background:linear-gradient(135deg,#ededed 20%,#f5a623 35%,#e94b5b 55%,#f2f2f2 70%,#c9c9c9)"></div>
      <div class="card-body"><div class="card-title">Editorial Magazine Layout</div><div class="card-type">Print</div><div class="card-by">by <b>EK Marlow</b></div></div>
      <div class="hire">Hire this Designer</div>
    </article>
    <article class="card" style="left:300px;top:348px">
      <div class="card-art" role="img" aria-label="Fashion website with colourful spectrum banner" style="background:linear-gradient(#3b3b3b 0 22%,#e6e6e6 23% 50%,#5a2a6a 51%,#c43a5a 65%,#e5e5e5 80%)"></div>
      <div class="card-body"><div class="card-title">Style Loft Website</div><div class="card-type">Web</div><div class="card-by">by <b>Solene88</b></div></div>
      <div class="hire">Hire this Designer</div>
    </article>
    <article class="card" style="left:562px;top:348px">
      <div class="card-art" role="img" aria-label="Autumn floral brand illustration in orange tones" style="background:radial-gradient(circle at 40% 50%,#ffffff 0 18%,#e85a1e 20%,#f4a33a 40%,#fbeee0 70%)"></div>
      <div class="card-body"><div class="card-title">Autumn Clothing Brand</div><div class="card-type">Logo + Print + Web</div><div class="card-by">by <b>Casper Wynn</b></div></div>
      <div class="hire">Hire this Designer</div>
    </article>
    <article class="card" style="left:825px;top:348px">
      <div class="card-art" role="img" aria-label="Kids learning website with teal paper background" style="background:radial-gradient(ellipse at 40% 70%,#4fb3c6,#2f8fa6 50%,#3a3a3a 80%)"></div>
      <div class="card-body"><div class="card-title">Kids Online Learning</div><div class="card-type">Web</div><div class="card-by">by <b>Farrell T</b></div></div>
      <div class="hire">Hire this Designer</div>
    </article>
  </main>

  <nav class="pager">
    <div class="pager-prev"><svg width="8" height="12" viewBox="0 0 8 12"><path d="M7 1L2 6l5 5" fill="none" stroke="#5c6670" stroke-width="2.2"/></svg>previous page</div>
    <div class="pager-next">next page<svg width="8" height="12" viewBox="0 0 8 12"><path d="M1 1l5 5-5 5" fill="none" stroke="#5c6670" stroke-width="2.2"/></svg></div>
  </nav>
</div>

<footer class="site-footer">© 2012 Copyright&nbsp; Corvelin Vividra Studio</footer>
</body>
</html>
```